Exterior cleaning company requires a eye catching a5 leaflet

we need some updated leaflet designs, a5 folded, we are targeting all exterior cleaning contracts, including roof cleaning & treatment, render cleaning & Treatment, driveways, block paving cleaning using the latest in low pressure cleaning technologies along side high pressure jetwashing. gutter clearance and flushing, water fed telescopic pole window cleaning of difficult to reach windows and high buildings. our website : www.tkbellowsec.co.uk facebook page: https://www.facebook.com/tkbellowsexteriorcareltd Instagram: https://www.instagram.com/tkbellowsec/ a quick google search of roof cleaning, soft washing etc will provide results of what we are doing

Target Market(s)

home owners, commercial clients

Font styles to use
Serif
Sans Serif

Requirements
Must have
• A5 Landscape folded leaflet, front page with company information and bullet points of main works : window & conservatory cleaning, roof cleaning & treatment, Render cleaning & treatment, pressure washing, soft washing, gutter clearing, pressure washing of patios, driveways, gutters, fascias (more info can be provided on techniques etc if required)

```html
<!DOCTYPE html>
<html lang="en">
<head>
<meta charset="utf-8">
<title>Harbrook Window Cleaning – Leaflet</title>
<link href="https://fonts.googleapis.com/css2?family=Montserrat:wght@700&family=Roboto+Condensed:wght@300;400;700&display=swap" rel="stylesheet">
<style>
  :root {
    --board: #b3b3b3;
    --label: #7a7a7a;
    --blue: #134a94;
    --blue-edge: #0b63ad;
    --yellow: #fcc313;
    --orange: #f6a21a;
    --ink: #1b1b1b;
    --white: #ffffff;
  }
  html, body {
    margin: 0;
    padding: 0;
    width: 1200px;
    height: 1015px;
    overflow: hidden;
    background: var(--board);
  }
  .board {
    position: relative;
    width: 1200px;
    height: 1015px;
  }
  .side-label {
    position: absolute;
    margin: 0;
    font-family: "Montserrat", sans-serif;
    font-weight: 700;
    font-size: 19px;
    letter-spacing: 0.5px;
    color: var(--label);
  }
  .spread {
    position: absolute;
    left: 72px;
    width: 1054px;
    height: 380px;
    display: block;
  }
  .spread--outer { top: 98px; }
  .spread--inner { top: 550px; }
  .spread text { font-family: "Roboto Condensed", sans-serif; }
  .t-bold { font-weight: 700; }
  .t-light { font-weight: 300; }
  .t-regular { font-weight: 400; }
  .fill-yellow { fill: var(--yellow); }
  .fill-blue { fill: var(--blue); }
  .fill-white { fill: var(--white); }
  .fill-ink { fill: var(--ink); }
</style>
</head>
<body>
<main class="board">

  <h2 class="side-label" style="left:76px;top:56px;">BACK</h2>
  <h2 class="side-label" style="left:595px;top:56px;">FRONT</h2>
  <h2 class="side-label" style="left:72px;top:516px;">INSIDE 1</h2>
  <h2 class="side-label" style="left:595px;top:516px;">INSIDE 2</h2>

  <!-- Outer spread: back panel and front cover -->
  <svg class="spread spread--outer" viewBox="0 0 1833 660" xmlns="http://www.w3.org/2000/svg">
    <defs>
      <g id="tick-yellow">
        <circle cx="0" cy="0" r="9" fill="none" stroke="#fcc313" stroke-width="3"/>
        <polyline points="-4,0 -1,4 5,-4" fill="none" stroke="#fcc313" stroke-width="3" stroke-linecap="round" stroke-linejoin="round"/>
      </g>
      <linearGradient id="house-soft" x1="0" y1="0" x2="0" y2="1">
        <stop offset="0" stop-color="#f4f5f6"/>
        <stop offset="0.6" stop-color="#e3e1de"/>
        <stop offset="1" stop-color="#eceeef"/>
      </linearGradient>
      <linearGradient id="house-photo" x1="0" y1="0" x2="0" y2="1">
        <stop offset="0" stop-color="#e8e4df"/>
        <stop offset="0.35" stop-color="#9a6a52"/>
        <stop offset="0.7" stop-color="#7a4a3a"/>
        <stop offset="1" stop-color="#3f6a2c"/>
      </linearGradient>
    </defs>

    <rect class="fill-blue" x="0" y="0" width="1833" height="660"/>

    <!-- back: faded house photo -->
    <polygon points="0,0 148,0 458,660 0,660" fill="url(#house-soft)" role="img" aria-label="Faded photo of a modern brick house with a patio and garden furniture"/>
    <polygon class="fill-yellow" points="148,0 191,0 497,660 458,660"/>

    <!-- slogan frame -->
    <polygon points="272,57 795,57 854,192 331,192" fill="none" stroke="#fcc313" stroke-width="2"/>
    <text class="t-bold fill-yellow" x="351" y="100" font-size="28" textLength="405" lengthAdjust="spacingAndGlyphs">HARBROOK WINDOW CLEANING IS</text>
    <text class="t-bold fill-yellow" x="351" y="134" font-size="23" textLength="455" lengthAdjust="spacingAndGlyphs">FERNMOUTH’S MOST RELIABLE, PROFESSIONAL</text>
    <text class="t-bold fill-yellow" x="351" y="167" font-size="23" textLength="201" lengthAdjust="spacingAndGlyphs">CLEANING COMPANY</text>

    <!-- call bar -->
    <polygon class="fill-yellow" points="312,276 722,276 772,380 362,380"/>
    <polygon class="fill-yellow" points="735,276 750,276 797,380 782,380"/>
    <g transform="translate(385,329)" fill="none" stroke="#134a94" stroke-width="5" stroke-linecap="round">
      <path d="M-10,-18 q-10,6 -6,20 q6,16 22,22 q10,2 16,-6 l-8,-8 q-6,6 -10,2 q-8,-6 -10,-14 q-2,-6 4,-8 z" fill="#134a94" stroke="none"/>
      <path d="M6,-16 a14,14 0 0 1 14,14"/>
      <path d="M8,-26 a24,24 0 0 1 22,22"/>
    </g>
    <text class="t-bold fill-blue" x="425" y="318" font-size="27" textLength="91" lengthAdjust="spacingAndGlyphs">CALL US</text>
    <text class="t-bold fill-blue" x="428" y="362" font-size="42" textLength="285" lengthAdjust="spacingAndGlyphs">US 01632 960418</text>

    <!-- experience -->
    <text class="t-bold fill-white" x="500" y="472" font-size="58">OVER</text>
    <text class="t-bold fill-yellow" x="500" y="548" font-size="84" textLength="312" lengthAdjust="spacingAndGlyphs">10 YEARS</text>
    <text class="t-bold fill-white" x="517" y="590" font-size="34" letter-spacing="14">EXPERIENCE</text>

    <!-- back logo -->
    <circle cx="75" cy="383" r="34" fill="none" stroke="#1b1b1b" stroke-width="1.5"/>
    <text class="t-bold fill-ink" x="123" y="382" font-size="36">Harbrook</text>
    <text class="t-regular fill-ink" x="123" y="410" font-size="19">Window Cleaning Ltd</text>

    <!-- back contact -->
    <text class="t-bold fill-ink" x="41" y="490" font-size="22">Contact us:</text>
    <g transform="translate(53,521)" fill="none" stroke="#f6a21a" stroke-width="3" stroke-linecap="round">
      <path d="M-6,-10 q-6,4 -3,12 q4,9 13,12 q6,1 9,-4 l-5,-5 q-3,3 -6,1 q-5,-4 -6,-8 q-1,-3 2,-5 z" fill="#f6a21a" stroke="none"/>
      <path d="M3,-9 a8,8 0 0 1 8,8"/>
    </g>
    <text class="t-bold fill-ink" x="73" y="534" font-size="37">01632 960 418</text>
    <g transform="translate(52,562)">
      <rect x="-7" y="-5" width="14" height="10" fill="#f6a21a"/>
      <polyline points="-7,-5 0,1 7,-5" fill="none" stroke="#fff" stroke-width="1.5"/>
    </g>
    <text class="t-bold fill-ink" x="73" y="569" font-size="20">INFO@HARBROOKWC.CO.UK</text>
    <g transform="translate(52,596)">
      <path d="M0,10 C-7,1 -7,-3 -7,-4 a7,7 0 0 1 14,0 c0,1 0,5 -7,14 z" fill="#f6a21a"/>
      <circle cx="0" cy="-4" r="2.5" fill="#fff"/>
    </g>
    <text class="t-bold fill-ink" x="73" y="605" font-size="20" textLength="359" lengthAdjust="spacingAndGlyphs">14 ALDER LANE, FERNMOUTH, FN4 2QT</text>

    <!-- front: main works list -->
    <g class="main-works">
      <use href="#tick-yellow" x="882" y="413"/>
      <text class="t-bold fill-white" x="904" y="421" font-size="23">SOFT WASHING</text>
      <use href="#tick-yellow" x="882" y="449"/>
      <text class="t-bold fill-white" x="904" y="457" font-size="23">GUTTER CLEARING</text>
      <use href="#tick-yellow" x="882" y="485"/>
      <text class="t-bold fill-white" x="904" y="493" font-size="23">PRESSURE WASHING</text>
      <use href="#tick-yellow" x="882" y="521"/>
      <text class="t-bold fill-white" x="904" y="529" font-size="23">WINDOWS &amp; CONSERVATORIES</text>
      <use href="#tick-yellow" x="882" y="557"/>
      <text class="t-bold fill-white" x="904" y="565" font-size="23">RENDER CLEANING &amp; TREATMENT</text>
      <use href="#tick-yellow" x="882" y="593"/>
      <text class="t-bold fill-white" x="904" y="601" font-size="23">ROOF CLEANING &amp; TREATMENT</text>
    </g>

    <!-- front: photo and stripes -->
    <polygon class="fill-yellow" points="936,0 973,0 1325,660 1288,660"/>
    <polygon points="973,0 1492,0 1805,660 1325,660" fill="url(#house-photo)" role="img" aria-label="Photo of a window cleaner using a water fed pole on a three-storey brick house"/>
    <polygon class="fill-yellow" points="1492,0 1526,0 1833,600 1833,660 1805,660"/>

    <!-- front logo -->
    <circle cx="1589" cy="90" r="29" fill="none" stroke="#ffffff" stroke-width="1.5"/>
    <text class="t-bold fill-white" x="1630" y="90" font-size="31">Harbrook</text>
    <text class="t-bold fill-white" x="1630" y="114" font-size="16">Window Cleaning Ltd</text>

    <!-- front title block -->
    <polygon points="1365,494 1380,494 1448,625 1433,625" fill="#1f2a12"/>
    <polygon class="fill-yellow" points="1390,494 1726,494 1795,625 1458,625"/>
    <text class="t-bold fill-blue" x="1603" y="542" font-size="48" text-anchor="middle">HARBROOK</text>
    <text class="t-bold fill-blue" x="1603" y="596" font-size="42" text-anchor="middle">Window Cleaning</text>
  </svg>

  <!-- Inner spread -->
  <svg class="spread spread--inner" viewBox="0 0 1833 662" xmlns="http://www.w3.org/2000/svg">
    <defs>
      <g id="tick-blue">
        <circle cx="0" cy="0" r="7" fill="none" stroke="#134a94" stroke-width="2.5"/>
        <polyline points="-3,0 -1,3 4,-3" fill="none" stroke="#134a94" stroke-width="2.5" stroke-linecap="round" stroke-linejoin="round"/>
      </g>
      <g id="tick-white">
        <circle cx="0" cy="0" r="7" fill="none" stroke="#ffffff" stroke-width="2.5"/>
        <polyline points="-3,0 -1,3 4,-3" fill="none" stroke="#ffffff" stroke-width="2.5" stroke-linecap="round" stroke-linejoin="round"/>
      </g>
      <linearGradient id="manor-photo" x1="0" y1="0" x2="0" y2="1">
        <stop offset="0" stop-color="#eceeef"/>
        <stop offset="0.2" stop-color="#8a5a44"/>
        <stop offset="0.6" stop-color="#6e4434"/>
        <stop offset="0.75" stop-color="#8c8a84"/>
        <stop offset="1" stop-color="#a8a59e"/>
      </linearGradient>
    </defs>

    <rect class="fill-yellow" x="0" y="0" width="1833" height="662"/>
    <polygon class="fill-blue" points="0,0 497,0 800,662 0,662"/>
    <polygon points="497,0 1025,0 1350,662 790,662" fill="url(#manor-photo)" role="img" aria-label="Photo of a large Victorian brick house with a cleaner working and a company van parked outside"/>
    <polygon points="497,0 512,0 822,662 800,662" fill="#0b63ad"/>
    <polygon points="1025,0 1058,0 1385,662 1350,662" fill="#f6a21a"/>

    <!-- left column -->
    <g class="services-left">
      <polygon class="fill-yellow" points="0,52 223,52 236,68 223,85 0,85"/>
      <use href="#tick-blue" x="43" y="69"/>
      <text class="t-bold fill-blue" x="59" y="76" font-size="22">External Windows</text>
      <text class="t-light fill-white" font-size="18">
        <tspan x="59" y="116">Our staff use the reach &amp; washes system otherwise known</tspan>
        <tspan x="59" y="139">as the ‘water fed pole’. A technique which compared to</tspan>
        <tspan x="59" y="162">traditional window cleaning, enabling us to reach your</tspan>
        <tspan x="59" y="185">windows and frames safely from the ground.</tspan>
      </text>

      <polygon class="fill-yellow" points="0,215 223,215 236,231 223,248 0,248"/>
      <use href="#tick-blue" x="43" y="232"/>
      <text class="t-bold fill-blue" x="59" y="239" font-size="22">Internal Windows</text>
      <text class="t-light fill-white" font-size="18">
        <tspan x="59" y="282">We clean internal windows and mirrors using the dragon fly system.</tspan>
        <tspan x="59" y="305">This method also using purified water can reach them hard to access</tspan>
        <tspan x="59" y="328">windows again safely from the ground</tspan>
      </text>

      <polygon class="fill-yellow" points="0,361 240,361 253,377 240,394 0,394"/>
      <use href="#tick-blue" x="43" y="378"/>
      <text class="t-bold fill-blue" x="59" y="385" font-size="22">Conservatory Roofs</text>
      <text class="t-light fill-white" font-size="18">
        <tspan x="59" y="426">Has your conservatory roof started to turn green, full of bird muck or dirt?</tspan>
        <tspan x="59" y="449">Our water pole method 99% of the time gets rid of all the dirt and grime build</tspan>
        <tspan x="59" y="472">up that’s left on your roof.</tspan>
      </text>

      <polygon class="fill-yellow" points="0,505 180,505 193,521 180,538 0,538"/>
      <use href="#tick-blue" x="43" y="522"/>
      <text class="t-bold fill-blue" x="59" y="529" font-size="22">Solar Panels</text>
      <text class="t-light fill-white" font-size="18">
        <tspan x="59" y="571">Using our access equipment we can clean your solar panels. Anything that blocks</tspan>
        <tspan x="59" y="594">the light transmission to your solar PV (or thermal) panels has the potential to lower</tspan>
        <tspan x="59" y="617">the performance.</tspan>
      </text>
    </g>

    <!-- right column -->
    <g class="services-right">
      <polygon class="fill-blue" points="1606,54 1833,54 1833,87 1606,87 1592,70"/>
      <text class="t-bold fill-white" x="1777" y="78" font-size="22" text-anchor="end">Fascias &amp; Gutters</text>
      <use href="#tick-white" x="1795" y="70"/>
      <text class="t-light fill-ink" font-size="18" text-anchor="end">
        <tspan x="1777" y="116">Our staff use the reach &amp; washes system otherwise known as the ‘water fed pole’. A</tspan>
        <tspan x="1777" y="139">technique which compared to traditional window cleaning, enabling us to reach your</tspan>
        <tspan x="1777" y="162">windows and frames safely from the ground.</tspan>
      </text>

      <polygon class="fill-blue" points="1586,190 1833,190 1833,223 1586,223 1572,206"/>
      <text class="t-bold fill-white" x="1777" y="214" font-size="22" text-anchor="end">Driveways &amp; Patios</text>
      <use href="#tick-white" x="1795" y="206"/>
      <text class="t-light fill-ink" font-size="18" text-anchor="end">
        <tspan x="1777" y="255">From small patio areas to large driveways we clean it all. Harbrook</tspan>
        <tspan x="1777" y="278">specialise in all driveway and patio cleaning from Indian stone, tarmac,</tspan>
        <tspan x="1777" y="301">concrete flags to block paving.</tspan>
      </text>

      <polygon class="fill-blue" points="1623,329 1833,329 1833,362 1623,362 1609,345"/>
      <text class="t-bold fill-white" x="1777" y="353" font-size="22" text-anchor="end">Gutter Cleaning</text>
      <use href="#tick-white" x="1795" y="345"/>
      <text class="t-light fill-ink" font-size="18" text-anchor="end">
        <tspan x="1774" y="393">Your property's gutters and downpipes accumulate all sorts of</tspan>
        <tspan x="1774" y="416">debris brought by the wind. Using our high reach vac we can</tspan>
        <tspan x="1774" y="439">clean the gutters safely from the ground eliminating any falls</tspan>
        <tspan x="1774" y="462">from height.</tspan>
      </text>

      <polygon class="fill-blue" points="1606,487 1833,487 1833,520 1606,520 1592,503"/>
      <text class="t-bold fill-white" x="1777" y="511" font-size="22" text-anchor="end">Pressure Washing</text>
      <use href="#tick-white" x="1795" y="503"/>
      <text class="t-light fill-ink" font-size="18" text-anchor="end">
        <tspan x="1777" y="550">We offer a wide range of pressure washing services from</tspan>
        <tspan x="1777" y="573">garden furniture to house roofs at competitive prices.</tspan>
        <tspan x="1777" y="596">Cleaning and restoration of all hard surfaces in both the</tspan>
        <tspan x="1777" y="619">domestic and commercial market</tspan>
      </text>
    </g>
  </svg>

</main>
</body>
</html>
```